Poem Handwritten by Veteran while in the jungle of Vietnam

My parents are celebrating their 50th wedding anniversary this year. I wanted to give them a very memorable gift. On my parents 2nd anniversary, my father was stationed in Vietnam. On that night he was in the jungle waiting till morning and wrote a poem to my mother using his pant leg as paper. I would like this poem to typographically designed to be framed and hung on the wall.

I have attached a picture of the poem below. It will need to be 11x14 when printed for framing. It would be great if there was background or artwork to make it more visually interesting, perhaps in a watercolor. My parents have a transitional style. I have attached some possible color schemes as well. Cool greens, blue, neutral grays, with hints of berries or highlights of yellow. These are just a guide, I would be open to your interpretations.

Thank you for your help. This will hopefully be a gift they will truly treasure as much as the poem itself.

Target Market(s)

My parents who are excited to be celebrating their 50th wedding anniversary. It should have a transitional, mature style.

Font styles to use
Serif
Script

Requirements
Must have
• The poem, typographically designed. There can be a mix of fonts, but legibility is critically important.
• Now that some designs have come through I wanted to give some more guidance of what I'm looking for. I want something that feels sophisticated and artistic.
Nice to have
• A background or art work, using the color schemes attached as a guide. I am really liking the designs that have a full color landscape artwork in the background. The fonts should be elegant and formal. I really like the romantic, muted colors. I had trouble finding similar projects online in the style I wanted until I cam across wedding invites. Those seem to be the most applicable. I've added pictures of some so you can get a sense of what I'm looking for. I am really liking the jungle foliage, starry skies or sunrises.
Should not have
• Cartoon caricatures, fonts that are too illegible when printed. I'm not liking anything whimsical. I don't like the very bright colors for this project.

```html
<!DOCTYPE html>
<html lang="en">
<head>
<meta charset="utf-8">
<title>Happy Anniversary Darling – Walter's Anniversary Poem</title>
<link rel="stylesheet" href="https://fonts.googleapis.com/css2?family=Josefin+Sans:wght@400&family=Yesteryear&family=Cookie&family=Courgette&family=Kalam:wght@300&display=swap">
<style>
  :root {
    --sky-top: #9fcb5f;
    --sky-low: #e3e18c;
    --hill-mid: #7fbb55;
    --forest: #3f7e3c;
    --forest-deep: #173826;
    --ink: #0f4a1f;
    --panel: rgba(28, 52, 40, 0.58);
    --poem-ink: #f4f1df;
  }
  * { margin: 0; padding: 0; box-sizing: border-box; }
  html, body { width: 943px; height: 1200px; overflow: hidden; }
  body { position: relative; background: var(--sky-top); }

  .landscape {
    position: absolute; inset: 0;
    background: linear-gradient(180deg,
      var(--sky-top) 0%, #c4d978 25%, var(--sky-low) 42%,
      var(--hill-mid) 52%, var(--forest) 72%, var(--forest-deep) 100%);
  }

  .title { position: absolute; inset: 0; color: var(--ink); }
  .title__happy {
    position: absolute; left: 172px; top: 70px;
    font-family: "Josefin Sans", sans-serif; font-size: 52px; letter-spacing: 8px;
    transform: rotate(-22deg); transform-origin: left bottom;
  }
  .title__main {
    position: absolute; left: 236px; top: 78px;
    font-family: "Yesteryear", cursive; font-size: 150px; line-height: 1;
  }
  .title__darling {
    position: absolute; left: 500px; top: 232px;
    font-family: "Cookie", cursive; font-size: 62px; line-height: 1;
  }
  .divider { position: absolute; left: 296px; top: 322px; }

  .heading {
    position: absolute; left: 0; width: 100%; text-align: center;
    font-family: "Courgette", cursive; color: var(--ink); font-size: 34px; line-height: 1;
  }
  .heading--date { top: 373px; }
  .heading--poem { top: 433px; }

  .poem-panel {
    position: absolute; left: 52px; top: 504px; width: 840px; height: 666px;
    background: var(--panel);
  }
  .poem-column {
    position: absolute; top: 24px; width: 420px; text-align: center;
    font-family: "Kalam", cursive; font-weight: 300; font-style: italic;
    font-size: 14px; line-height: 21.6px; color: var(--poem-ink);
  }
  .poem-column--left { left: 0; }
  .poem-column--right { left: 420px; }
  .stanza { margin-bottom: 21px; }
</style>
</head>
<body>
  <div class="landscape" role="img" aria-label="Soft green mountain landscape with a forest of pine trees and birds in flight"></div>

  <header class="title">
    <div class="title__happy">HAPPY</div>
    <div class="title__main">Anniversary</div>
    <div class="title__darling">Darling</div>
    <svg class="divider" width="352" height="16" viewBox="0 0 352 16" aria-hidden="true">
      <path d="M0 8 Q80 5 150 8 Q80 11 0 8Z" fill="#0f1f12"/>
      <circle cx="178" cy="8" r="6" fill="#0f1f12"/>
      <path d="M352 8 Q272 5 202 8 Q272 11 352 8Z" fill="#0f1f12"/>
    </svg>
  </header>

  <h1 class="heading heading--date">20 July 1970, Monday, LZ Professional</h1>
  <h2 class="heading heading--poem">Walter's Anniversary Poem</h2>

  <main class="poem-panel">
    <div class="poem-column poem-column--left">
      <p class="stanza">Life's journey began with a challenge,<br>It was heralded far and near.<br>The road led on forever,<br>Its completion was known to be dear.</p>
      <p class="stanza">From the garden of light it proceeded,<br>To the valley of shadows it led.<br>Thorns and thistles adorned it,<br>Past abyss and crevice it sped.</p>
      <p class="stanza">The brave surged forward with courage,<br>The wise undaunted pressed on.<br>The mighty held high their banner,<br>We all awaited the dawn.</p>
      <p class="stanza">Though the pitfalls and hazards were many,<br>The pathway was clearly in view.<br>Straight and sure it glided,<br>Its course we knew to be true.</p>
      <p class="stanza">I knew you, Sweetheart, beforehand,<br>So precious and sweet were you.<br>Our moments of bliss were priceless,<br>Each day brought us joy anew.</p>
      <p class="stanza">The call to progression beckoned,<br>At last I would have my chance—<br>To clasp you to me forever,<br>And seal our divine romance.</p>
    </div>
    <div class="poem-column poem-column--right">
      <p class="stanza">I eagerly started the journey,<br>Though with sorrow, I left you behind.<br>With courage and faith I continued,<br>For I knew, that you later I'd find.</p>
      <p class="stanza">I diligently searched for you. Darling.<br>The roadway was both bleak and fair.<br>Though the years grew long in number,<br>I did not give up in despair.</p>
      <p class="stanza">At last in the distance I saw you.<br>So beautiful, lovely, and sweet!<br>Your attention I struggled to capture,<br>Your love I wrested to meet.</p>
      <p class="stanza">What rapture was mine in fulfillment,<br>As now together we stand.<br>To cherish and love each other.<br>While our plans and dreams expand.</p>
      <p class="stanza">I love you, Darling, forever,<br>My life you have made replete.<br>Our eternal mansion beckons,<br>Your love has made it complete.</p>
    </div>
  </main>
</body>
</html>
```